Brightwell - Self Development Mobile App

Basic Instructions
1. please create an android app screen design for me, in figma, for my new app “Brightwell” based on this pencil drawing (Subjects.jpg)
2. Create the color pallet based on the colors of the logo (#fcd354 and #5dc9b7) and also add shades based on these colors based on material design.
3. the background should be white.
4. Use material design
Get Inspired by wordhopper design and calmnest design
These are the directions i provided for the programmer on how this screen will work:
top bar:
back icon on left (show if you are in a category and press to go back one category)
name of the field in middle in bold
share icon for sharing the current subject on the right before the drop down menu
3 dot icon on the right (drop down menu)
2nd top bar:
fire icon on left for streak (how many days straight did you do a lesson)
star icon a bit after it (how many lessons did you pass)
circles section:
each category will get a section
each category will have a small star with a number that shows how many stars the user has from that category
each category will have an icon before it
under each category there will be circles for all the subjects under that category
scroll horizontally to see more subjects
each subject will have the amount stars gained from it (like the circles of the fields in the fields screen)
scroll down to see more fields with their subjects
note that the order of the subjects and categories should be based on the practial/spiritual score that the user has been assigned based on the initial wizard
More Notes
1. the scribbles in the circles under the following categories (Dreams, Sub-Concious, Feeling)) are just place filers. Please add example content based on the content in the circles that are under “Memory” category
2. There are more sections after Feeling so users should be able to scroll down to see more sections
3. There are more categories to the right so under each section
Final Thoughts
Maybe its better to have rounded cornered squares instead of circles. You choose what you think is best.
After you have created the Subjects screen and I like it, then I'll give you instructions for the other 5 screens.
Target Market(s)
general public, adults 18-80
Font styles to use
Look and feel
Each slider illustrates characteristics of the customer's brand and the style your logo design should communicate.

```html
<!DOCTYPE html>
<html lang="en">
<head>
<meta charset="utf-8">
<title>Brightwell – Self Development Mobile App</title>
<link href="https://fonts.googleapis.com/css2?family=Roboto:wght@400;500;700;900&display=swap" rel="stylesheet">
<style>
:root{
  --board:#dafff9;
  --teal:#5dc9b7;
  --yellow:#fcd354;
  --ink:#1e1e1e;
  --dark:#3a3a3a;
  --grey:#969696;
  --light:#d9d9d9;
  --cream:#fdf5e6;
  --red:#ff3d3d;
  --red-mid:#d98276;
  --red-soft:#ffbdb5;
  --green:#12d62b;
  --teal-soft:#a0ddd3;
  --white:#ffffff;
}
*{box-sizing:border-box;margin:0;padding:0}
html,body{width:1200px;height:1200px;overflow:hidden}
body{background:var(--board);font-family:"Roboto",sans-serif;color:var(--ink);position:relative}
.abs{position:absolute}

.headline{left:96px;top:54px;font-size:44px;font-weight:700;line-height:66px;letter-spacing:.5px}
.cursor-icon{left:736px;top:133px}

.screen{position:absolute;width:146px;height:304px;background:var(--white);border-radius:14px;overflow:hidden;box-shadow:0 2px 6px rgba(0,0,0,.12)}
.status{position:absolute;top:0;left:0;right:0;height:18px;font-size:6px;padding:8px 10px 0;display:flex;justify-content:space-between}
.status .dots{width:14px;height:4px;background:var(--dark);border-radius:2px;margin-top:1px}
.appbar{position:absolute;top:0;left:0;right:0;height:40px;background:var(--yellow)}
.appbar .title{position:absolute;left:0;right:0;top:25px;text-align:center;font-size:8px;color:var(--dark)}
.appbar .back{position:absolute;left:7px;top:27px;width:5px;height:5px;border-left:1px solid var(--dark);border-bottom:1px solid var(--dark);transform:rotate(45deg)}
.appbar .more{position:absolute;right:6px;top:26px;font-size:8px;line-height:6px;color:var(--dark)}
.appbar .share{position:absolute;right:14px;top:27px}

.stats{position:absolute;top:50px;left:8px;display:flex;gap:10px;font-size:6px;align-items:center}
.stats span{display:flex;align-items:center;gap:3px}
.drop{width:7px;height:9px;border-radius:50% 50% 50% 50%/60% 60% 40% 40%;background:var(--teal-soft)}
.star{width:9px;height:9px;background:var(--yellow);clip-path:polygon(50% 0,62% 35%,100% 38%,70% 60%,80% 100%,50% 78%,20% 100%,30% 60%,0 38%,38% 35%)}

.divider{position:absolute;left:4px;right:4px;display:flex;align-items:center;gap:4px;font-size:8px;color:var(--dark)}
.divider::before,.divider::after{content:"";flex:1;height:1px;background:var(--light)}
.node{position:absolute;width:32px;height:32px;border-radius:50%;margin:-16px 0 0 -16px}
.node.done{background:var(--yellow);border:3px solid var(--teal-soft)}
.node.todo{background:var(--light);border:3px solid #ececec}
.plant{position:absolute;width:44px;height:52px;border-radius:40% 40% 30% 30%;background:linear-gradient(var(--yellow),var(--teal))}
.percent{position:absolute;font-size:11px;font-weight:900;font-style:italic;color:var(--teal);letter-spacing:1px}

.progress{position:absolute;top:50px;left:8px;width:108px;height:4px;border-radius:2px;background:var(--light)}
.progress i{display:block;width:22px;height:4px;border-radius:2px;background:var(--teal)}
.qstreak{position:absolute;top:47px;right:8px;font-size:5px;display:flex;gap:2px;align-items:center}
.question{position:absolute;top:65px;left:7px;right:10px;font-size:6px;line-height:9px}
.speaker{position:absolute;top:90px;left:8px;width:11px;height:11px;border-radius:50%;background:var(--yellow)}
.option{position:absolute;width:58px;height:66px;border-radius:5px;background:var(--light);font-size:6px;color:var(--dark);display:flex;align-items:center;justify-content:center;text-align:center}
.option.wrong{background:var(--red-mid);color:var(--white)}
.option.right{background:var(--teal);color:var(--white)}
.btn{position:absolute;left:7px;right:7px;height:15px;border-radius:4px;font-size:6.5px;font-weight:500;display:flex;align-items:center;justify-content:center}
.feedback{position:absolute;left:0;right:0;bottom:0;height:72px;padding:8px 9px}
.feedback b{display:block;font-size:7px;font-weight:500;margin-bottom:3px}
.feedback p{font-size:4.5px;line-height:7px;color:var(--dark)}
.feedback.bad{background:var(--red-soft)}
.feedback.good{background:var(--teal-soft)}

.tile{position:absolute;width:55px;height:48px;border-radius:6px;background:var(--teal);padding:26px 5px 0;font-size:5px;font-weight:500;color:var(--dark)}
.tile.active{background:var(--yellow)}
.tile small{display:block;font-size:3px;font-weight:400;line-height:4px;margin-top:1px}
.tile .ico{position:absolute;left:5px;top:5px;width:12px;height:12px;border-radius:3px;background:var(--dark)}
.tile .count{position:absolute;right:5px;top:6px;font-size:3.5px;display:flex;gap:1px;align-items:center}
.tile .count .star{width:6px;height:6px}
.navbar{position:absolute;left:0;right:0;bottom:0;height:28px;background:var(--yellow);display:flex;justify-content:space-around;padding-top:5px;font-size:4.5px;font-weight:500}
.navbar span{display:flex;flex-direction:column;align-items:center;gap:2px}
.navbar i{width:8px;height:8px;border-radius:2px;background:var(--dark)}

.section{position:absolute;left:6px;right:6px}
.section h3{font-size:7.5px;font-weight:500;display:flex;justify-content:space-between;align-items:center}
.section h3 span{display:flex;align-items:center;gap:2px;font-size:5px;font-weight:400}
.section p{font-size:4.5px;line-height:6px;color:var(--dark);margin-top:2px;width:75px}
.cards{position:absolute;left:6px;display:flex;gap:4px}
.card{width:50px;height:35px;border-radius:3px;background:var(--teal);padding:13px 4px 0;font-size:5px;color:var(--dark);position:relative;flex-shrink:0}
.card.active{background:var(--yellow)}
.card small{display:block;font-size:3px;line-height:4px;margin-top:1px}
.card .star{position:absolute;left:4px;top:4px;width:5px;height:5px}

.label{font-weight:700}
.fonts-title{left:81px;top:982px;font-size:26px;font-weight:700;letter-spacing:-.5px}
.fonts-heading{left:81px;top:1024px;font-size:27px;font-weight:500}
.fonts-body{left:81px;top:1065px;font-size:15.5px}
.color-title{left:393px;top:944px;font-size:27px;font-weight:700;letter-spacing:-.5px}
.swatches{display:flex;gap:8px}
.swatches i{width:40px;height:40px;border-radius:3px;display:block}
.sw-label{font-size:15px;font-weight:700;letter-spacing:-.3px}
.thanks{left:760px;top:1010px;width:370px;text-align:center;font-size:68px;font-weight:900;letter-spacing:-2.5px}
.thanks-sub{left:760px;top:1104px;width:370px;text-align:center;font-size:22px;line-height:27px;color:var(--dark)}
</style>
</head>
<body>

<h1 class="abs headline">Brightwell - Self Development<br>Mobile App : UX / UI Design</h1>
<svg class="abs cursor-icon" width="30" height="26" viewBox="0 0 30 26" aria-hidden="true"><path d="M2 4 L28 2 L18 24 L15 12 Z" fill="var(--dark)"/></svg>

<!-- Home: fields -->
<div class="screen" style="left:76px;top:230px">
  <div class="status"><span>9:41</span><span class="dots"></span></div>
  <div class="abs" style="left:7px;top:30px;font-size:7px;font-weight:700;color:var(--dark)">Welcome Back Sam</div>
  <div class="abs" style="right:8px;top:30px;font-size:4px;display:flex;gap:4px;align-items:center"><span class="drop" style="width:5px;height:6px"></span>2 <span class="star" style="width:6px;height:6px"></span>34</div>
  <div class="abs" style="left:9px;top:50px;font-size:6px">Explore Your Inner Fields</div>
  <div class="abs" style="left:9px;top:58px;font-size:3px;color:var(--dark)">Start your journey across mind, body, and spirit.</div>
  <div class="tile active" style="left:9px;top:72px"><span class="ico"></span><span class="count"><i class="star"></i>0</span>Mind<small>Sharpen focus, calm the mind.</small></div>
  <div class="tile" style="left:72px;top:72px"><span class="ico"></span><span class="count"><i class="star"></i>34</span>Body<small>Tune in with your physical self.</small></div>
  <div class="tile" style="left:9px;top:128px"><span class="ico"></span><span class="count"><i class="star"></i>34</span>Hobbies<small>Discover what lights you up.</small></div>
  <div class="tile" style="left:72px;top:128px"><span class="ico"></span><span class="count"><i class="star"></i>34</span>Finance<small>Build clarity around abundance.</small></div>
  <div class="tile" style="left:9px;top:184px"><span class="ico"></span><span class="count"><i class="star"></i>34</span>Spiritual<small>Grow your inner light.</small></div>
  <div class="tile" style="left:72px;top:184px"><span class="ico"></span><span class="count"><i class="star"></i>34</span>Recommended<small>Your personalized journey.</small></div>
  <div class="tile" style="left:9px;top:240px"><span class="ico"></span><span class="count"><i class="star"></i>34</span>social</div>
  <div class="tile" style="left:72px;top:240px"><span class="ico"></span><span class="count"><i class="star"></i>34</span>Professional</div>
  <nav class="navbar"><span><i></i>Fields</span><span><i></i>Explore</span><span><i></i>Account</span></nav>
</div>

<!-- Mind: categories -->
<div class="screen" style="left:256px;top:230px">
  <div class="appbar"><div class="status"><span>9:41</span><span class="dots"></span></div><span class="back"></span><div class="title">Mind</div></div>
  <div class="stats"><span><i class="drop"></i>2</span><span><i class="star"></i>34</span></div>
  <div class="section" style="top:74px"><h3>Memory<span><i class="star"></i>7</span></h3><p>Sharpen your recall and attention.</p></div>
  <div class="cards" style="top:100px"><div class="card active"><i class="star"></i>Foundation<small>Basics of how memory works</small></div><div class="card"><i class="star"></i>Names<small>Techniques to remember names</small></div><div class="card"><i class="star"></i>Numbers<small>Remembering numerical info</small></div></div>
  <div class="section" style="top:144px"><h3>Dreams<span><i class="star"></i>7</span></h3><p>Decode the messages hidden in your dreams.</p></div>
  <div class="cards" style="top:176px"><div class="card"><i class="star"></i>Foundation<small>Basics of how memory works</small></div><div class="card"><i class="star"></i>Names<small>Techniques to remember names</small></div><div class="card"><i class="star"></i>Numbers<small>Remembering numerical info</small></div></div>
  <div class="section" style="top:220px"><h3>Subconscious<span><i class="star"></i>7</span></h3><p style="width:95px">Tap into the quiet patterns shaping your thoughts and choices.</p></div>
  <div class="cards" style="top:251px"><div class="card"><i class="star"></i>Foundation<small>Basics of how memory works</small></div><div class="card"><i class="star"></i>Names<small>Techniques to remember names</small></div><div class="card"><i class="star"></i>Numbers<small>Remembering numerical info</small></div></div>
  <div class="section" style="top:293px"><h3>Feeling<span><i class="star"></i>7</span></h3></div>
</div>

<!-- Memory path: complete -->
<div class="screen" style="left:436px;top:230px">
  <div class="appbar"><div class="status"><span>9:41</span><span class="dots"></span></div><span class="back"></span><div class="title">Memory</div><svg class="share" width="7" height="6" viewBox="0 0 7 6" aria-hidden="true"><path d="M1 1 L6 3 L1 5" fill="none" stroke="var(--dark)"/></svg><span class="more">⋮</span></div>
  <div class="stats"><span><i class="drop"></i>2</span><span><i class="star"></i>34</span></div>
  <div class="divider" style="top:73px">Foundation</div>
  <div class="node done" style="left:73px;top:106px" role="img" aria-label="Lesson badge: door"></div>
  <div class="node done" style="left:56px;top:142px" role="img" aria-label="Lesson badge: book"></div>
  <div class="node done" style="left:46px;top:178px" role="img" aria-label="Lesson badge: hand"></div>
  <div class="node done" style="left:56px;top:213px" role="img" aria-label="Lesson badge: book"></div>
  <div class="node done" style="left:73px;top:249px" role="img" aria-label="Lesson badge: star"></div>
  <div class="plant" style="left:81px;top:136px" role="img" aria-label="Potted plant in full bloom"></div>
  <div class="percent" style="left:82px;top:196px">100%</div>
  <div class="divider" style="top:277px">Names</div>
</div>

<!-- Test 1: unanswered -->
<div class="screen" style="left:616px;top:230px">
  <div class="appbar"><div class="status"><span>9:41</span><span class="dots"></span></div><span class="back"></span><div class="title">Test 1</div></div>
  <div class="progress"><i></i></div><div class="qstreak"><i class="drop" style="width:5px;height:6px"></i>2</div>
  <p class="question">Which of the following names are associated with memory techniques?</p>
  <span class="speaker"></span>
  <div class="option" style="left:7px;top:106px">Method of Loci</div>
  <div class="option" style="left:72px;top:106px">Passive Reading</div>
  <div class="option" style="left:7px;top:181px">Skimming</div>
  <div class="option" style="left:72px;top:181px">Highlighting</div>
  <div class="btn" style="top:272px;background:var(--yellow)">CHECK</div>
</div>

<!-- Test 1: wrong -->
<div class="screen" style="left:796px;top:230px">
  <div class="appbar"><div class="status"><span>9:41</span><span class="dots"></span></div><span class="back"></span><div class="title">Test 1</div></div>
  <div class="progress"><i></i></div><div class="qstreak"><i class="drop" style="width:5px;height:6px"></i>2</div>
  <p class="question">Which of the following names are associated with memory techniques?</p>
  <span class="speaker"></span>
  <div class="option" style="left:7px;top:106px">Method of Loci</div>
  <div class="option" style="left:72px;top:106px">Passive Reading</div>
  <div class="option" style="left:7px;top:181px">Skimming</div>
  <div class="option wrong" style="left:72px;top:181px">Highlighting</div>
  <div class="feedback bad"><b style="color:var(--red)">✕ <span style="color:var(--dark)">Wrong:</span></b><p>Try again! Passive reading isn't an active memorization method.</p></div>
  <div class="btn" style="top:272px;background:var(--red-mid);color:var(--dark)">GOT IT</div>
</div>

<!-- Test 1: correct -->
<div class="screen" style="left:976px;top:230px">
  <div class="appbar"><div class="status"><span>9:41</span><span class="dots"></span></div><span class="back"></span><div class="title">Test 1</div></div>
  <div class="progress"><i></i></div><div class="qstreak"><i class="drop" style="width:5px;height:6px"></i>2</div>
  <p class="question">Which of the following names are associated with memory techniques?</p>
  <span class="speaker"></span>
  <div class="option right" style="left:7px;top:106px">Method of Loci</div>
  <div class="option" style="left:72px;top:106px">Passive Reading</div>
  <div class="option" style="left:7px;top:181px">Skimming</div>
  <div class="option" style="left:72px;top:181px">Highlighting</div>
  <div class="feedback good"><b><span style="color:var(--green)">✓</span> Correct:</b><p>Method of Loci is a spatial memory technique.</p></div>
  <div class="btn" style="top:272px;background:var(--teal);color:var(--dark)">CONTINUE</div>
</div>

<!-- Memory path progress states -->
<div class="screen" style="left:76px;top:581px">
  <div class="appbar"><div class="status"><span>9:41</span><span class="dots"></span></div><span class="back"></span><div class="title">Memory</div><svg class="share" width="7" height="6" viewBox="0 0 7 6" aria-hidden="true"><path d="M1 1 L6 3 L1 5" fill="none" stroke="var(--dark)"/></svg><span class="more">⋮</span></div>
  <div class="stats"><span><i class="drop"></i>2</span><span><i class="star"></i>34</span></div>
  <div class="divider" style="top:73px">Foundation</div>
  <div class="node done" style="left:73px;top:106px" role="img" aria-label="Lesson badge: door"></div>
  <div class="node todo" style="left:56px;top:142px" role="img" aria-label="Locked lesson badge"></div>
  <div class="node todo" style="left:46px;top:178px" role="img" aria-label="Locked lesson badge"></div>
  <div class="node todo" style="left:56px;top:213px" role="img" aria-label="Locked lesson badge"></div>
  <div class="node todo" style="left:73px;top:249px" role="img" aria-label="Locked lesson badge"></div>
  <div class="plant" style="left:87px;top:160px;width:30px;height:36px" role="img" aria-label="Potted seedling"></div>
  <div class="percent" style="left:86px;top:204px">20%</div>
  <div class="divider" style="top:277px">Names</div>
</div>

<div class="screen" style="left:256px;top:581px">
  <div class="appbar"><div class="status"><span>9:41</span><span class="dots"></span></div><span class="back"></span><div class="title">Memory</div><svg class="share" width="7" height="6" viewBox="0 0 7 6" aria-hidden="true"><path d="M1 1 L6 3 L1 5" fill="none" stroke="var(--dark)"/></svg><span class="more">⋮</span></div>
  <div class="stats"><span><i class="drop"></i>2</span><span><i class="star"></i>34</span></div>
  <div class="divider" style="top:73px">Foundation</div>
  <div class="node done" style="left:73px;top:106px" role="img" aria-label="Lesson badge: door"></div>
  <div class="node done" style="left:56px;top:142px" role="img" aria-label="Lesson badge: book"></div>
  <div class="node todo" style="left:46px;top:178px" role="img" aria-label="Locked lesson badge"></div>
  <div class="node todo" style="left:56px;top:213px" role="img" aria-label="Locked lesson badge"></div>
  <div class="node todo" style="left:73px;top:249px" role="img" aria-label="Locked lesson badge"></div>
  <div class="plant" style="left:86px;top:150px;width:32px;height:46px" role="img" aria-label="Potted young plant"></div>
  <div class="percent" style="left:84px;top:204px">40%</div>
  <div class="divider" style="top:277px">Names</div>
</div>

<div class="screen" style="left:436px;top:581px">
  <div class="appbar"><div class="status"><span>9:41</span><span class="dots"></span></div><span class="back"></span><div class="title">Memory</div><svg class="share" width="7" height="6" viewBox="0 0 7 6" aria-hidden="true"><path d="M1 1 L6 3 L1 5" fill="none" stroke="var(--dark)"/></svg><span class="more">⋮</span></div>
  <div class="stats"><span><i class="drop"></i>2</span><span><i class="star"></i>34</span></div>
  <div class="divider" style="top:73px">Foundation</div>
  <div class="node done" style="left:73px;top:106px" role="img" aria-label="Lesson badge: door"></div>
  <div class="node done" style="left:56px;top:142px" role="img" aria-label="Lesson badge: book"></div>
  <div class="node done" style="left:46px;top:178px" role="img" aria-label="Lesson badge: hand"></div>
  <div class="node todo" style="left:56px;top:213px" role="img" aria-label="Locked lesson badge"></div>
  <div class="node todo" style="left:73px;top:249px" role="img" aria-label="Locked lesson badge"></div>
  <div class="plant" style="left:85px;top:142px;width:34px;height:54px" role="img" aria-label="Potted growing plant"></div>
  <div class="percent" style="left:84px;top:204px">60%</div>
  <div class="divider" style="top:277px">Names</div>
</div>

<div class="screen" style="left:616px;top:581px">
  <div class="appbar"><div class="status"><span>9:41</span><span class="dots"></span></div><span class="back"></span><div class="title">Memory</div><svg class="share" width="7" height="6" viewBox="0 0 7 6" aria-hidden="true"><path d="M1 1 L6 3 L1 5" fill="none" stroke="var(--dark)"/></svg><span class="more">⋮</span></div>
  <div class="stats"><span><i class="drop"></i>2</span><span><i class="star"></i>34</span></div>
  <div class="divider" style="top:73px">Foundation</div>
  <div class="node done" style="left:73px;top:106px" role="img" aria-label="Lesson badge: door"></div>
  <div class="node done" style="left:56px;top:142px" role="img" aria-label="Lesson badge: book"></div>
  <div class="node done" style="left:46px;top:178px" role="img" aria-label="Lesson badge: hand"></div>
  <div class="node done" style="left:56px;top:213px" role="img" aria-label="Lesson badge: book"></div>
  <div class="node todo" style="left:73px;top:249px" role="img" aria-label="Locked lesson badge"></div>
  <div class="plant" style="left:82px;top:138px;width:40px;height:58px" role="img" aria-label="Potted plant starting to bloom"></div>
  <div class="percent" style="left:84px;top:204px">80%</div>
  <div class="divider" style="top:277px">Names</div>
</div>

<div class="screen" style="left:796px;top:581px">
  <div class="appbar"><div class="status"><span>9:41</span><span class="dots"></span></div><span class="back"></span><div class="title">Memory</div><svg class="share" width="7" height="6" viewBox="0 0 7 6" aria-hidden="true"><path d="M1 1 L6 3 L1 5" fill="none" stroke="var(--dark)"/></svg><span class="more">⋮</span></div>
  <div class="stats"><span><i class="drop"></i>2</span><span><i class="star"></i>34</span></div>
  <div class="divider" style="top:73px">Foundation</div>
  <div class="node done" style="left:73px;top:106px" role="img" aria-label="Lesson badge: door"></div>
  <div class="node done" style="left:56px;top:142px" role="img" aria-label="Lesson badge: book"></div>
  <div class="node done" style="left:46px;top:178px" role="img" aria-label="Lesson badge: hand"></div>
  <div class="node done" style="left:56px;top:213px" role="img" aria-label="Lesson badge: book"></div>
  <div class="node done" style="left:73px;top:249px" role="img" aria-label="Lesson badge: star"></div>
  <div class="plant" style="left:80px;top:136px" role="img" aria-label="Potted plant in full bloom"></div>
  <div class="percent" style="left:80px;top:204px">100%</div>
  <div class="divider" style="top:277px">Names</div>
</div>

<!-- Type and colour -->
<h2 class="abs fonts-title">Font Use:</h2>
<p class="abs fonts-heading">H1 ,H2 ,H3:&nbsp; Roboto</p>
<p class="abs fonts-body">body, <span style="font-weight:500">button</span> &nbsp;: &nbsp;Roboto</p>

<h2 class="abs color-title">Color:</h2>
<div class="abs swatches" style="left:393px;top:994px"><i style="background:var(--teal)"></i><i style="background:var(--yellow)"></i><i style="background:var(--dark)"></i><i style="background:var(--grey)"></i><i style="background:var(--light)"></i><i style="background:var(--cream)"></i></div>
<p class="abs sw-label" style="left:393px;top:1041px">Error / Red</p>
<div class="abs swatches" style="left:393px;top:1067px"><i style="background:var(--red)"></i><i style="background:var(--red-mid)"></i><i style="background:var(--red-soft)"></i></div>
<p class="abs sw-label" style="left:393px;top:1114px">Success / Green</p>
<div class="abs swatches" style="left:393px;top:1140px"><i style="background:var(--green)"></i><i style="background:var(--teal)"></i><i style="background:var(--teal-soft)"></i></div>

<p class="abs thanks">Thank you</p>
<p class="abs thanks-sub">Your feedback matters to us. Let us know what you think!</p>

</body>
</html>
```